Law Firm Business Card

This is a business card for a law firm that serves US military and veterans.

The card must have ONLY the following (we want an uncluttered look):

- Company logo (PNG, GIF, JPEG copies uploaded)
- A tagline reading: "a law firm for service members and veterans"
- My name and title: "Martin Okello" and "Attorney"
- My email: "martin.okello@harborlinecounsel.com"
- My number: "855-FILE-NOW (345-3669)"

We are looking for a clean, simple layout with only the above information, likely printed on a bright white cotton stock. The font of our logo is DIN 1451, and the font used on our website is Helvetica Neue. The color of our logo is #336699, and we probably want the tagline in that color also, and my contact information in a dark grey. Please review our website at www.harborlinecounsel.com to ensure your card design complements our website style.

Thanks and we look forward to seeing your submissions.

A few notes:

- Two-sided submissions are ok
- Please don't add graphics (scales of justice, judges hammer, etc)

```html
<!DOCTYPE html>
<html lang="en">
<head>
<meta charset="utf-8">
<title>Harborline Counsel — Business Card</title>
<link rel="stylesheet" href="https://fonts.googleapis.com/css2?family=Arimo:wght@400;700&display=swap">
<style>
  :root {
    --brand-blue: #336699;
    --ink-grey: #4a4a4a;
    --soft-grey: #7a7a7a;
    --card-white: #ffffff;
    --backdrop: #e4e1dc;
  }
  * { box-sizing: border-box; margin: 0; padding: 0; }
  html, body {
    width: 1200px;
    height: 848px;
    overflow: hidden;
    background: var(--backdrop);
    font-family: "Arimo", "Helvetica Neue", Helvetica, Arial, sans-serif;
  }
  .stage {
    width: 1200px;
    height: 848px;
    display: flex;
    align-items: center;
    justify-content: center;
  }
  .business-card {
    position: relative;
    width: 1050px;
    height: 600px;
    background: var(--card-white);
    box-shadow: 0 6px 24px rgba(0, 0, 0, 0.12);
    overflow: hidden;
  }
  .brand-band {
    position: absolute;
    left: 0;
    top: 0;
    width: 250px;
    height: 100%;
    background: var(--brand-blue);
  }
  .brand-block {
    position: absolute;
    top: 70px;
    right: 70px;
    display: flex;
    flex-direction: column;
    align-items: flex-end;
    gap: 12px;
    color: var(--brand-blue);
  }
  .wordmark {
    display: flex;
    align-items: center;
    gap: 16px;
    font-weight: 700;
    font-size: 46px;
    line-height: 1;
    letter-spacing: 0.02em;
    text-transform: uppercase;
  }
  .wordmark-dot {
    width: 18px;
    height: 18px;
    background: var(--brand-blue);
  }
  .tagline {
    font-weight: 400;
    font-size: 22px;
    letter-spacing: 0.03em;
  }
  .contact-block {
    position: absolute;
    left: 300px;
    top: 260px;
  }
  .person-name {
    color: var(--brand-blue);
    font-weight: 700;
    font-size: 36px;
    line-height: 1.15;
  }
  .person-title {
    color: var(--soft-grey);
    font-weight: 400;
    font-size: 34px;
    letter-spacing: 0.03em;
    margin-top: 4px;
  }
  .contact-lines {
    list-style: none;
    margin-top: 34px;
  }
  .contact-line {
    color: var(--ink-grey);
    font-size: 28px;
    line-height: 1.6;
    white-space: nowrap;
  }
  .contact-label {
    display: inline-block;
    width: 38px;
    color: var(--brand-blue);
    font-weight: 700;
  }
</style>
</head>
<body>
  <main class="stage">
    <article class="business-card">
      <div class="brand-band"></div>

      <header class="brand-block">
        <div class="wordmark">
          <span class="wordmark-dot"></span>
          <span class="wordmark-name">Harborline Counsel</span>
        </div>
        <p class="tagline">a law firm for service members and veterans</p>
      </header>

      <section class="contact-block">
        <h1 class="person-name">Martin Okello</h1>
        <p class="person-title">Attorney</p>
        <ul class="contact-lines">
          <li class="contact-line"><span class="contact-label">m</span>martin.okello@harborlinecounsel.com</li>
          <li class="contact-line"><span class="contact-label">p</span>855-FILE-NOW (345-3669)</li>
        </ul>
      </section>
    </article>
  </main>
</body>
</html>
```